Design Brenza Kolto Freight Series M 1.6 2022

We are looking for a design for our Brenza Kolto White.
We Tovrilomark BV are a company with several webshops.

Please include the logos of the most important webshops in the design.
Supporting images of installation may also be incorporated.

```html
<!DOCTYPE html>
<html lang="en">
<head>
<meta charset="utf-8">
<title>Tovrilomark BV – Brenza Kolto Freight Series M 1.6 2022 wrap</title>
<link rel="stylesheet" href="https://fonts.googleapis.com/css2?family=Montserrat:wght@600;700&display=swap">
<style>
  :root {
    --navy: #1d3a6e;
    --navy-dark: #142a52;
    --blue: #1f6fc0;
    --sky: #4aa3df;
    --green: #5fb43a;
    --lime: #8cc63f;
    --charcoal: #2a2d33;
    --white: #ffffff;
    --paper: #f4f5f7;
  }
  * { margin: 0; padding: 0; box-sizing: border-box; }
  html, body { width: 1200px; height: 829px; overflow: hidden; background: var(--paper); }
  .wrap-design {
    position: relative;
    width: 1200px;
    height: 829px;
    font-family: "Montserrat", Arial, sans-serif;
  }
  .wrap-panel {
    position: absolute;
    left: 100px; top: 220px;
    width: 1000px; height: 380px;
    background: var(--white);
    overflow: hidden;
  }
  .headline {
    position: absolute;
    left: 505px; top: 22px;
    font-size: 34px;
    font-weight: 700;
    color: var(--navy);
    white-space: nowrap;
  }
  .photo {
    position: absolute;
    border-radius: 4px;
  }
  .photo--technician {
    left: 560px; top: 62px; width: 395px; height: 160px;
    background: linear-gradient(120deg, #e6e9ee 0%, #c9a56a 35%, #8fa6c2 65%, #dfe3e8 100%);
  }
  .photo--fittings {
    left: 100px; top: 148px; width: 310px; height: 120px;
    background: linear-gradient(100deg, #eceef1 0%, #c79b5e 45%, #b9c2cc 80%, #eceef1 100%);
  }
  .swoosh { position: absolute; left: 0; top: 0; }
  .brand {
    position: absolute;
    left: 400px; top: 198px;
    display: flex; align-items: center; gap: 14px;
  }
  .brand__dot {
    width: 30px; height: 30px; border-radius: 50%;
    background: var(--blue);
  }
  .brand__name {
    font-size: 44px;
    font-weight: 700;
    color: var(--navy);
    white-space: nowrap;
  }
  .services {
    position: absolute;
    left: 300px; top: 286px;
    display: flex; gap: 26px;
    font-size: 17px; font-weight: 600;
    color: var(--white);
    list-style: none;
  }
  .services li::before { content: "•"; margin-right: 10px; }
  .contact {
    position: absolute;
    left: 270px; top: 318px;
    width: 560px; height: 28px;
    background: var(--charcoal);
    border-radius: 14px;
    display: flex; justify-content: space-around; align-items: center;
    font-size: 14px; font-weight: 600;
    color: var(--white);
  }
</style>
</head>
<body>
<div class="wrap-design">
  <section class="wrap-panel">
    <div class="photo photo--technician" role="img" aria-label="Photo of hands connecting cables and brass fittings on an installation panel"></div>
    <div class="photo photo--fittings" role="img" aria-label="Photo of hands tightening brass pipe fittings"></div>

    <svg class="swoosh" width="1000" height="380" viewBox="0 0 1000 380" aria-hidden="true">
      <path d="M0 230 C 250 240, 500 200, 1000 120 L1000 380 L0 380 Z" fill="var(--lime)"/>
      <path d="M0 250 C 280 258, 560 215, 1000 150 L1000 380 L0 380 Z" fill="var(--white)"/>
      <path d="M0 262 C 300 262, 600 230, 1000 175 L1000 380 L0 380 Z" fill="var(--green)"/>
      <path d="M0 272 C 320 270, 620 245, 1000 200 L1000 380 L0 380 Z" fill="var(--sky)"/>
      <path d="M0 282 C 330 280, 640 260, 1000 225 L1000 380 L0 380 Z" fill="var(--blue)"/>
      <path d="M0 292 C 340 290, 660 275, 1000 250 L1000 380 L0 380 Z" fill="var(--navy)"/>
      <path d="M0 355 L1000 330 L1000 380 L0 380 Z" fill="var(--green)"/>
    </svg>

    <h1 class="headline">We Tovrilomark BV</h1>

    <div class="brand">
      <span class="brand__dot"></span>
      <span class="brand__name">Tovrilomark</span>
    </div>

    <ul class="services">
      <li>Installations</li>
      <li>Maintenance</li>
      <li>Repairs</li>
    </ul>

    <div class="contact">
      <span class="contact__phone">+31 10 555 0182</span>
      <span class="contact__web">www.tovrilomark.nl</span>
    </div>
  </section>
</div>
</body>
</html>
```